New Business Card Design Project

I would like to purchase a customized version of a design you have previously submitted - https://www.plomarket.com/design/7724163<br/><br/>I would like to incorporate the attached Images for my fitness company "TalvrenPro Athletics". My initial services is personal training and athletic performance. I would like a card that has one a shiny black side with the silver logo and the side with a white background utilizing the gold logo. On the white side, put "Sports Performance and Functional Strength Training" under the logo.
Industry/Entity Type
Fitness
Contact Information for Business Card
Marcus Tolley
Owner and Trainer
555.273.8492
marcus.tolley@talvrenproathletics.com
Look and feel
Each slider illustrates characteristics of the customer's brand and the style your logo design should communicate.

```html
<!DOCTYPE html>
<html lang="en">
<head>
<meta charset="UTF-8">
<title>TalvrenPro Athletics — Business Card</title>
<link href="https://fonts.googleapis.com/css2?family=Open+Sans:wght@400;600;700&display=swap" rel="stylesheet">
<style>
  :root {
    --page-bg: #e9e7e3;
    --card-black: #141414;
    --card-black-soft: #2b2b2b;
    --card-white: #ffffff;
    --silver: #c9c9c9;
    --gold: #9c8652;
    --ink: #1c1c1c;
    --ink-soft: #3a3a3a;
  }
  * { box-sizing: border-box; margin: 0; padding: 0; }
  html, body {
    width: 1200px; height: 1200px; overflow: hidden;
    background: var(--page-bg);
    font-family: "Open Sans", Arial, sans-serif;
  }
  .canvas {
    width: 1200px; height: 1200px;
    display: flex; flex-direction: column; align-items: center; justify-content: center;
    gap: 60px;
  }
  .card {
    width: 840px; height: 480px; position: relative; overflow: hidden;
    box-shadow: 0 10px 28px rgba(0,0,0,0.22);
  }
  .card--front {
    background: linear-gradient(135deg, var(--card-black-soft) 0%, var(--card-black) 45%, #000 100%);
    display: flex; align-items: center; justify-content: center;
  }
  .brand { display: flex; flex-direction: column; align-items: center; gap: 18px; }
  .brand-mark {
    width: 150px; height: 150px; border-radius: 50%;
    border: 6px solid currentColor;
  }
  .brand-name {
    font-weight: 700; font-size: 34px; letter-spacing: 4px; text-transform: uppercase;
    white-space: nowrap;
  }
  .card--front .brand { color: var(--silver); }

  .card--back { background: var(--card-white); }
  .card--back .brand {
    position: absolute; right: 60px; top: 44px; width: 400px; color: var(--gold);
    gap: 14px;
  }
  .card--back .brand-mark { width: 160px; height: 160px; }
  .card--back .brand-name { font-size: 26px; letter-spacing: 3px; }
  .brand-tagline {
    font-weight: 600; font-size: 14px; line-height: 1.3; color: var(--ink-soft);
    text-align: center; white-space: nowrap;
  }

  .person { position: absolute; left: 70px; top: 120px; color: var(--ink); }
  .person-name { font-weight: 700; font-size: 34px; line-height: 1.2; }
  .person-title { font-weight: 600; font-size: 17px; color: var(--ink-soft); margin-top: 4px; }

  .contact { position: absolute; left: 70px; bottom: 52px; color: var(--ink); list-style: none; }
  .contact-item {
    display: flex; align-items: center; gap: 16px;
    font-weight: 600; font-size: 26px; line-height: 1.55; white-space: nowrap;
  }
  .contact-icon { width: 28px; height: 28px; fill: var(--ink); flex: none; }
</style>
</head>
<body>
<main class="canvas">
  <section class="card card--front" aria-label="Card front">
    <div class="brand">
      <div class="brand-mark"></div>
      <span class="brand-name">TalvrenPro Athletics</span>
    </div>
  </section>

  <section class="card card--back" aria-label="Card back">
    <div class="person">
      <p class="person-name">Marcus Tolley</p>
      <p class="person-title">Owner and Trainer</p>
    </div>

    <div class="brand">
      <div class="brand-mark"></div>
      <span class="brand-name">TalvrenPro Athletics</span>
      <p class="brand-tagline">Sports Performance and Functional Strength Training</p>
    </div>

    <ul class="contact">
      <li class="contact-item">
        <svg class="contact-icon" viewBox="0 0 24 24" aria-hidden="true"><path d="M6.6 10.8a15.1 15.1 0 0 0 6.6 6.6l2.2-2.2c.3-.3.7-.4 1-.2 1.1.4 2.3.6 3.6.6.6 0 1 .4 1 1V20c0 .6-.4 1-1 1A17 17 0 0 1 3 4c0-.6.4-1 1-1h3.5c.6 0 1 .4 1 1 0 1.3.2 2.5.6 3.6.1.3 0 .7-.2 1z"/></svg>
        <span>555.273.8492</span>
      </li>
      <li class="contact-item">
        <svg class="contact-icon" viewBox="0 0 24 24" aria-hidden="true"><path d="M2 6.2V19h20V6.2l-10 7.6z M2.6 5h18.8L12 12.2z"/></svg>
        <span>marcus.tolley@talvrenproathletics.com</span>
      </li>
    </ul>
  </section>
</main>
</body>
</html>
```